Medical device box for kits used for self testing purposes. Attractive simplistic design

Looking for a design that will go on a box that offer multiple range of medical testing ranging from hormones panel to diabetes and thyroid hormones. looking for something attractive and simple to go on a box 6 x 4.5 x 1 inches. attached are some examples from competitors. and our logo that be incorporated with the design.
Picture of the boxes have been attached, pick the color you think goes best with your design.

Target Market(s)

Patients and regular consumers

Industry/Entity Type

Medical

Requirements
Nice to have
• Simple design that is eye catching

```html
<!DOCTYPE html>
<html lang="en">
<head>
<meta charset="utf-8">
<title>Norvel Test Kit Box Panel</title>
<link rel="stylesheet" href="https://fonts.googleapis.com/css2?family=Fredoka:wght@600&family=Roboto:wght@400&display=swap">
<style>
  :root {
    --backdrop: #d4d4d4;
    --panel: #f5f5fa;
    --navy: #12173a;
    --yellow: #f9d71c;
    --orange: #f6b13c;
    --green: #3fb58a;
    --teal: #12a594;
    --grey-node: #c9c9cc;
    --blue: #3a9be0;
    --tagline: #7a7a7e;
    --contact: #1b1f3b;
  }
  * { margin: 0; padding: 0; box-sizing: border-box; }
  html, body {
    width: 935px; height: 1200px; overflow: hidden;
    background: var(--backdrop);
  }
  .box-front {
    position: absolute; left: 30px; top: 271px;
    width: 875px; height: 657px;
    background: var(--panel);
    overflow: hidden;
  }
  .network {
    position: absolute;
  }
  .network--warm {
    left: 0; top: 0; width: 200px; height: 185px;
    background: radial-gradient(ellipse at 40% 40%, rgba(249,200,60,.45), rgba(246,177,60,.15) 55%, rgba(245,245,250,0) 75%);
  }
  .network--green {
    left: 0; top: 415px; width: 230px; height: 242px;
    background: radial-gradient(ellipse at 35% 45%, rgba(63,181,138,.38), rgba(18,165,148,.12) 55%, rgba(245,245,250,0) 75%);
  }
  .network--grey {
    left: 200px; top: 540px; width: 300px; height: 117px;
    background: radial-gradient(ellipse at 50% 70%, rgba(180,180,186,.38), rgba(200,200,204,.12) 55%, rgba(245,245,250,0) 78%);
  }
  .network--blue {
    left: 520px; top: 300px; width: 355px; height: 357px;
    background: radial-gradient(ellipse at 75% 75%, rgba(58,155,224,.38), rgba(120,190,230,.12) 55%, rgba(245,245,250,0) 78%);
  }
  .brand {
    position: absolute; left: 540px; top: 62px;
    display: flex; align-items: center; gap: 14px;
  }
  .brand__dot {
    width: 52px; height: 52px; border-radius: 50%;
    background: var(--yellow);
  }
  .brand__name {
    font-family: "Fredoka", sans-serif; font-weight: 600;
    font-size: 84px; line-height: 1; color: var(--navy);
    letter-spacing: -1px;
  }
  .title-band {
    position: absolute; left: 0; top: 272px;
    width: 652px; height: 94px;
    background: var(--navy);
  }
  .title-band__text {
    position: absolute; left: 92px; top: 2px;
    font-family: "Fredoka", sans-serif; font-weight: 600;
    font-size: 80px; line-height: 90px; color: #fff;
    letter-spacing: -1px;
  }
  .tagline {
    position: absolute; left: 95px; top: 383px;
    font-family: "Roboto", sans-serif; font-weight: 400;
    font-size: 27px; color: var(--tagline);
  }
  .contact {
    position: absolute; top: 550px;
    display: flex; align-items: center; gap: 5px;
    font-family: "Roboto", sans-serif; font-size: 18px;
    color: var(--contact);
  }
  .contact--web { left: 259px; }
  .contact--mail { left: 530px; }
  .contact svg { display: block; }
</style>
</head>
<body>
  <main class="box-front">
    <div class="network network--warm" role="img" aria-label="Yellow and orange molecule network decoration"></div>
    <div class="network network--green" role="img" aria-label="Green and teal molecule network decoration"></div>
    <div class="network network--grey" role="img" aria-label="Grey molecule network decoration"></div>
    <div class="network network--blue" role="img" aria-label="Blue molecule network decoration"></div>

    <div class="brand">
      <span class="brand__dot"></span>
      <span class="brand__name">Norvel</span>
    </div>

    <div class="title-band">
      <h1 class="title-band__text">LOREM IPSUM</h1>
    </div>
    <p class="tagline">MEET YOUR BODY’S POTENTIAL</p>

    <p class="contact contact--web">
      <svg width="16" height="16" viewBox="0 0 16 16" aria-hidden="true">
        <g fill="none" stroke="#f9d71c" stroke-width="1.2">
          <circle cx="8" cy="8" r="6.5"/>
          <ellipse cx="8" cy="8" rx="3" ry="6.5"/>
          <line x1="1.5" y1="8" x2="14.5" y2="8"/>
          <line x1="2.5" y1="4.5" x2="13.5" y2="4.5"/>
          <line x1="2.5" y1="11.5" x2="13.5" y2="11.5"/>
        </g>
      </svg>
      norvelhealth.com
    </p>
    <p class="contact contact--mail">
      <svg width="22" height="15" viewBox="0 0 22 15" aria-hidden="true">
        <rect x="0.5" y="0.5" width="21" height="14" fill="#f9d71c"/>
        <polyline points="0.5,0.5 11,8.5 21.5,0.5" fill="none" stroke="#fff" stroke-width="1.3"/>
      </svg>
      care@norvelhealth.com
    </p>
  </main>
</body>
</html>
```